IT services web page design

Hello!

We need new design for our web site, obviously :)

Our company is service oriented and we are maintaining, configuring and fixing problems for IT + selling other internet related services.

Our speciality are in area of internet services (web, dns, email, databases, backup...) and internet servers technology.

We also provide service and sales of Zentor Apps and Halvorix Quorvo365 for which we are certified by Zentor and Halvorix.

Other services that we provide (not so in focus) are: VPS hosting, remote backup, web hosting, vexalink fixing...

People mostly call us when they have a problems and this is core idea that new web site has to communicate - We can fix your server / web / email problems, save your money and as* :)

Our team have 15+ years experience with all range of internet technology + bunch of certificates from Halvorix and Tandix [we need to show people we have certificates].
Our qualities: experience, knowledge, delivery on time

In start we will not have blog section, but we need it in future. We also need place for plonkit feeds on web site.

Depth of the site should be max. level 2.

This site will go out in two languages so we need switch button on page from pone language to another.

Target Market(s)

small and mid size business that use internet services for daily operations and main business

Industry/Entity Type

Internet

Requirements
Must have
• * design should be in the way that responsive web could be made

Nice to have
• Long format will be OK for us. Like today pages that list all services and benefits on one loooong web page...

Logo is in attachment. It will be nice to have it on web site but if you find it not appropriate you can change it or put another one.

```html
<!DOCTYPE html>
<html lang="en">
<head>
<meta charset="utf-8">
<title>Nerida grupa – IT Solutions</title>
<link href="https://fonts.googleapis.com/css2?family=Yanone+Kaffeesatz:wght@300;400&family=Ubuntu:wght@300;400&display=swap" rel="stylesheet">
<style>
:root{
  --blue:#0b7fd0;
  --blue-bright:#1aa0ea;
  --blue-deep:#0a6cc0;
  --accent:#1a9ad6;
  --heading:#4a4a4a;
  --text:#5c5c5c;
  --line:#dcdcdc;
  --footer:#e6e6e6;
  --white:#ffffff;
}
*{box-sizing:border-box;margin:0;padding:0}
html,body{width:1108px;height:1200px;overflow:hidden;background:var(--white)}
body{position:relative;font-family:"Ubuntu",sans-serif;color:var(--text)}
.topbar{position:absolute;left:0;top:0;width:1108px;height:7px;background:var(--blue-deep)}
.site-header{position:absolute;left:0;top:7px;width:1108px;height:104px;background:linear-gradient(#fafafa,#e9e9e9)}
.brand{position:absolute;left:111px;top:34px;display:flex;align-items:center;gap:10px;font-family:"Ubuntu",sans-serif;font-weight:400;font-size:26px;color:#1b1b1b}
.brand-dot{width:60px;height:60px;border-radius:50%;background:var(--blue-bright)}
.main-nav{position:absolute;left:391px;top:41px;display:flex;gap:23px;font-family:"Yanone Kaffeesatz",sans-serif;font-size:15px;color:#555;letter-spacing:.2px}
.hero{position:absolute;left:0;top:111px;width:1108px;height:444px;background:radial-gradient(ellipse at 55% 45%,#2fb0f2 0%,#1291de 45%,#0a72c4 100%)}
.hero-art{position:absolute;left:111px;top:41px;width:424px;height:360px;background:linear-gradient(90deg,#8e9498,#e4e6e8 30%,#b9bdc0 55%,#e8eaeb 75%,#8d9295);border-radius:4px;opacity:.9}
.hero-title{position:absolute;left:602px;top:158px;font-family:"Yanone Kaffeesatz",sans-serif;font-weight:400;font-size:34px;color:var(--white);letter-spacing:.5px}
.hero-text{position:absolute;left:602px;top:194px;width:395px;font-family:"Yanone Kaffeesatz",sans-serif;font-weight:300;font-size:17px;line-height:22px;color:var(--white);text-transform:uppercase}
.hero-btn{position:absolute;left:601px;top:283px;width:93px;height:35px;background:linear-gradient(#f2f2f2,#c9c9c9);font-family:"Yanone Kaffeesatz",sans-serif;font-size:17px;color:#8a8a8a;text-align:center;line-height:35px}
.slider-dots{position:absolute;left:945px;top:403px;display:flex;gap:5px}
.slider-dots span{width:10px;height:10px;border-radius:50%;background:#9aa4ab;border:1px solid #d0d6da}
.slider-dots span.is-active{background:#3a3f43}
.section-title{font-family:"Yanone Kaffeesatz",sans-serif;font-weight:400;font-size:20px;color:var(--heading);text-transform:uppercase;letter-spacing:.3px}
.section-title em{font-style:normal;color:var(--accent)}
.welcome{position:absolute;left:111px;top:568px;width:581px}
.welcome .section-title,.services .section-title{padding-bottom:10px;border-bottom:1px solid var(--line)}
.welcome p{font-size:11.5px;line-height:15.7px;font-weight:300;color:var(--text);margin-top:15px;text-align:justify}
.welcome p+p{margin-top:15px}
.services{position:absolute;left:720px;top:568px;width:277px}
.services ul{list-style:none;margin-top:9px}
.services li{font-size:11.5px;font-weight:300;height:27.7px;line-height:27.7px;padding-left:22px;position:relative}
.services li::before{content:"";position:absolute;left:3px;top:10px;border-left:5px solid var(--accent);border-top:3.5px solid transparent;border-bottom:3.5px solid transparent}
.rule{position:absolute;left:111px;top:818px;width:886px;height:3px;background:#cfcfcf}
.feature{position:absolute;top:836px;width:277px}
.feature .section-title{font-size:19px}
.feature-media{margin-top:15px;width:277px;height:106px}
.feature p{margin-top:7px;font-size:11.5px;line-height:15.2px;font-weight:300;text-align:justify;height:89px;overflow:hidden}
.feature p .lead{color:var(--accent);font-size:12.5px}
.btn{display:inline-block;margin-top:9px;width:74px;height:27px;background:var(--blue-deep);color:var(--white);font-size:11px;line-height:27px;text-align:center}
.col-sep{position:absolute;top:838px;width:1px;height:242px;background:var(--line)}
.site-footer{position:absolute;left:0;top:1127px;width:1108px;height:73px;background:var(--footer)}
.copyright{position:absolute;left:114px;top:33px;font-family:Arial,sans-serif;font-size:11.5px;color:#444}
.social{position:absolute;left:851px;top:28px;display:flex;gap:9px}
.social span{width:30px;height:30px;border-radius:50%}
</style>
</head>
<body>
<div class="topbar"></div>
<header class="site-header">
  <div class="brand"><span>Nerida grupa</span><span class="brand-dot"></span></div>
  <nav class="main-nav">
    <span>HOME</span><span>VIRTUAL PRIVATE SERVER</span><span>MAINTENANCE OF COMPUTER SYSTEMS</span><span>ZENTOR APPS</span><span>HOSTING SERVICES</span><span>CONTACT</span>
  </nav>
</header>

<section class="hero">
  <div class="hero-art" role="img" aria-label="Three silver server towers"></div>
  <h1 class="hero-title">VIRTUAL PRIVATE SERVER (VPS)</h1>
  <p class="hero-text">Are you developing advanced websites and applications or run a web studio that provides its clients with complete services including web hosting, then VPS is a great solution.</p>
  <div class="hero-btn">LEARN MORE</div>
  <div class="slider-dots"><span></span><span class="is-active"></span><span></span></div>
</section>

<section class="welcome">
  <h2 class="section-title">Welcome to <em>Nerida-grupa !</em></h2>
  <p>We are a company that configures and maintains web servers and builds advanced IT solutions to support their business.</p>
  <p>Our clients are companies that uses its advanced IT solutions in the form of dedicated servers, virtual servers (VPS), private networks (VPN) and online backup on Fenestra and Tandix platforms.As an added value services are available for 00-24 resolved, the removal of all the problems in order to ensure smooth operation of the services and related services.We have the knowledge and 15 + years of experience in the field of installation, configuration and maintenance services .</p>
  <p>Our employees their experience and knowledge gained are leading their own IT company (one of the first Internet service providers in Croatia) and working in telecom companies. For this reason, know and understand the importance of stability, security and financial feasibility of each project or solutions that are delivered to our customers.</p>
</section>

<aside class="services">
  <h2 class="section-title">Our services</h2>
  <ul>
    <li>Fenestra servers</li>
    <li>Tandix servers</li>
    <li>Web services (HTTP, HTTPS, SSL ...)</li>
    <li>DNS and domain</li>
    <li>Email Service</li>
    <li>Firewall and VPN Solutions</li>
    <li>Backup (on-site, off-site, on-line solutions)</li>
  </ul>
</aside>

<div class="rule"></div>

<article class="feature" style="left:111px">
  <h3 class="section-title">Maintenance of computer systems</h3>
  <div class="feature-media" role="img" aria-label="Small figurines of workers repairing a keyboard" style="background:linear-gradient(135deg,#9a9a9a,#d8d8d8 45%,#a7a7a7 70%,#c9643a)"></div>
  <p>Computers are many companies have become very important tool for the work and any delays, malfunctions or failure of the "instruments of labor" has a direct impact on the company's operations. Often this influence is in the form of low productivity and poor, breaking the limits and the worst - of direct financial losses.</p>
  <span class="btn">READ MORE</span>
</article>
<div class="col-sep" style="left:401px"></div>

<article class="feature" style="left:415px">
  <h3 class="section-title">Zentor Apps</h3>
  <div class="feature-media" role="img" aria-label="Cloud with connected user groups and a security shield" style="background:radial-gradient(ellipse at 50% 60%,#bfe6fb 0%,#49b6ef 45%,#10a0e8 100%)"></div>
  <p>Computers are many companies have become very important tool for the work and any delays, malfunctions or failure of the "instruments of labor" has a direct impact on the company's operations. Often this influence is in the form of low productivity and poor, breaking the limits and the worst - of direct financial losses.</p>
  <span class="btn">READ MORE</span>
</article>
<div class="col-sep" style="left:705px"></div>

<article class="feature" style="left:719px">
  <h3 class="section-title">Latest news</h3>
  <div class="feature-media" role="img" aria-label="Office apps shown on a laptop, tablet and phone" style="background:linear-gradient(90deg,#d7e7f3,#f4f4f4 40%,#2b2b2b 55%,#efefef 75%,#e46b5c)"></div>
  <p><span class="lead">Computers are many companies have become very important tool for the work and any delays,</span> malfunctions or failure of the "instruments of labor" has a direct impact on the company's operations. Often this influence is in the form of low productivity and poor, breaking the limits and the worst - of direct financial losses.</p>
  <span class="btn">READ MORE</span>
</article>

<footer class="site-footer">
  <p class="copyright">© 2013 nerida-grupa |&nbsp; All Rights Reserved.</p>
  <div class="social">
    <span style="background:#3b5a9a"></span>
    <span style="background:#2aa9e0"></span>
    <span style="background:#d9302a"></span>
    <span style="background:#e2473a"></span>
  </div>
</footer>
</body>
</html>
```